looking for sleek business card to standout from the crowd!

We are a young biotechnology company looking to help you personalize your health through understanding your genetic make up. We need you help in making a clean but sleek business card design using our new logo. The goal? Any time we give our cards out, people say "nice card!" The feel we are going for is "modern-techy". We don't want to come across as an old, giant pharma company, but not trying to be a hipster either.

Target Market(s)

healthcare and biotechnology industry.

Industry/Entity Type

Biotechnology

Contact Information for Business Card

Info to include on the card will be NAME, TITLE, EMAIL, PHONE. The companies website (www.corvalinbio.com) should also be on the card some where. Would like the logo, when printed, to be raised.

Requirements
Must have
• The logo we have attached in the color it is in. Fonts for text should lean toward more professional/tech.
Nice to have
• Prefer white/light color background
Should not have
• cartoons, landscape backgrounds images.

```html
<!DOCTYPE html>
<html lang="en">
<head>
<meta charset="utf-8">
<title>Corvalin Business Card</title>
<link rel="stylesheet" href="https://fonts.googleapis.com/css2?family=Roboto:wght@400;500;700&display=swap">
<style>
  :root {
    --backdrop: #2e6e80;
    --card-light: #ffffff;
    --card-dark: #1a1a1a;
    --brand-blue: #1a70bf;
    --brand-green: #8cc63f;
    --text-grey: #555555;
    --mark-grey: #9a9a9a;
    --mark-dark: #0f0f0f;
  }
  html, body {
    margin: 0;
    width: 1200px;
    height: 1200px;
    overflow: hidden;
    background: var(--backdrop);
    font-family: "Roboto", Arial, sans-serif;
  }
  .card {
    position: absolute;
    left: 162px;
    width: 876px;
    height: 500px;
  }
  .card--front { top: 84px; background: var(--card-light); }
  .card--back { top: 615px; background: var(--card-dark); }

  .brand {
    position: absolute;
    display: flex;
    align-items: center;
    gap: 14px;
  }
  .brand__name {
    font-weight: 700;
    letter-spacing: 1px;
  }
  .card--front .brand { left: 62px; top: 56px; }
  .card--front .brand__name { font-size: 76px; color: var(--brand-blue); }
  .card--front .brand__dot { width: 108px; height: 108px; border-radius: 50%; background: var(--brand-green); }

  .card--back .brand { left: 50%; top: 50%; transform: translate(-50%, -50%); }
  .card--back .brand__name { font-size: 84px; color: var(--mark-grey); }
  .card--back .brand__dot {
    width: 138px; height: 138px; border-radius: 50%;
    background: var(--mark-dark);
  }

  .person {
    position: absolute;
    right: 62px;
    top: 232px;
    text-align: right;
  }
  .person__name { font-size: 35px; font-weight: 500; color: var(--brand-blue); line-height: 1.1; }
  .person__title { font-size: 24px; color: var(--text-grey); margin-top: 4px; }

  .divider {
    position: absolute;
    left: 60px;
    right: 58px;
    top: 330px;
    height: 2px;
    background: var(--brand-blue);
  }

  .contact {
    position: absolute;
    left: 62px;
    top: 362px;
    margin: 0;
    padding: 0;
    list-style: none;
    font-size: 22px;
    color: var(--text-grey);
  }
  .contact li { display: flex; align-items: center; gap: 10px; height: 31px; }
  .contact svg { width: 20px; height: 20px; flex: none; }

  .address {
    position: absolute;
    right: 62px;
    top: 394px;
    text-align: right;
    font-size: 22px;
    color: var(--text-grey);
    line-height: 31px;
    font-style: normal;
  }
</style>
</head>
<body>
  <section class="card card--front">
    <div class="brand">
      <span class="brand__name">CORVALIN</span>
      <span class="brand__dot"></span>
    </div>
    <div class="person">
      <div class="person__name">Daniel Hartwell</div>
      <div class="person__title">President</div>
    </div>
    <div class="divider"></div>
    <ul class="contact">
      <li>
        <svg viewBox="0 0 20 20"><path fill="#8cc63f" d="M4 1l4 4-2 3c1 2 3 4 5 5l3-2 4 4-3 3C8 18 2 12 1 4z"/></svg>
        800 555 0142
      </li>
      <li>
        <svg viewBox="0 0 20 20"><rect x="1" y="4" width="18" height="12" fill="#8cc63f"/><path d="M1 4l9 7 9-7M1 16l7-6M19 16l-7-6" fill="none" stroke="#fff" stroke-width="1.4"/></svg>
        support@corvalinbio.com
      </li>
      <li>
        <svg viewBox="0 0 20 20" fill="none" stroke="#8cc63f" stroke-width="1.5"><circle cx="10" cy="10" r="8.5"/><ellipse cx="10" cy="10" rx="4" ry="8.5"/><path d="M1.5 10h17M3 5.5h14M3 14.5h14"/></svg>
        www.corvalinbio.com
      </li>
    </ul>
    <address class="address">2450 Harbor Way Suite 300<br>Oakland, CA 94607</address>
  </section>

  <section class="card card--back">
    <div class="brand">
      <span class="brand__name">CORVALIN</span>
      <span class="brand__dot"></span>
    </div>
  </section>
</body>
</html>
```